" Empresa focada em seguros pessoais, tais como seguro saúde, vida, previdência e odontológico, oferecendo segurança e agilidade na contrataçao e manutençao e também qualidade de vida. "

```html
<!DOCTYPE html>
<html lang="pt-BR">
<head>
<meta charset="utf-8">
<title>Envelope Saco – BrisaCorp</title>
<link rel="stylesheet" href="https://fonts.googleapis.com/css2?family=Titillium+Web:wght@400;600&display=swap">
<style>
  :root {
    --page: #e9e9e9;
    --paper: #ffffff;
    --navy: #0d3a85;
    --cyan: #25bccd;
    --ink-light: #ffffff;
    --muted: #6f8fa8;
  }
  html, body {
    margin: 0;
    padding: 0;
    width: 1200px;
    height: 1200px;
    overflow: hidden;
    background: var(--page);
  }
  .canvas {
    position: relative;
    width: 1200px;
    height: 1200px;
    font-family: "Titillium Web", sans-serif;
  }
  .envelope-art {
    position: absolute;
    inset: 0;
  }
  .brand {
    position: absolute;
    display: flex;
    align-items: center;
    gap: 10px;
  }
  .brand-dot {
    width: 26px;
    height: 26px;
    border-radius: 50%;
  }
  .brand-text { line-height: 1; }
  .brand-name {
    font-weight: 600;
    font-size: 30px;
    letter-spacing: 0.2px;
  }
  .brand-tagline {
    font-size: 10px;
    margin-top: 3px;
    letter-spacing: 0.6px;
  }
  .brand--front { left: 258px; top: 340px; }
  .brand--front .brand-dot { background: var(--cyan); }
  .brand--front .brand-name { color: var(--navy); }
  .brand--front .brand-tagline { color: var(--muted); }
  .brand--back { left: 720px; top: 918px; }
  .brand--back .brand-dot { background: var(--ink-light); }
  .brand--back .brand-name,
  .brand--back .brand-tagline { color: var(--ink-light); }
  .contact {
    position: absolute;
    right: 125px;
    top: 900px;
    text-align: right;
    color: var(--ink-light);
    font-size: 10px;
    line-height: 13px;
  }
  .contact p { margin: 0; }
  .contact .web { font-weight: 600; }
</style>
</head>
<body>
<main class="canvas">
  <svg class="envelope-art" width="1200" height="1200" viewBox="0 0 1200 1200">
    <defs>
      <clipPath id="front-clip"><rect x="0" y="0" width="629" height="1200"/></clipPath>
      <clipPath id="back-clip"><rect x="629" y="0" width="571" height="1200"/></clipPath>
    </defs>
    <!-- front side: flap, side tab, bottom tab, panel -->
    <path class="front-flap" d="M118 262 L118 228 Q118 211 135 211 L612 211 Q629 211 629 228 L629 262 Z" fill="var(--navy)"/>
    <path class="front-side-tab" d="M118 300 L104 318 L104 918 L118 936 Z" fill="var(--paper)"/>
    <path class="front-bottom-tab" d="M150 972 L170 992 L590 992 L610 972 Z" fill="var(--paper)"/>
    <rect class="front-panel" x="118" y="262" width="511" height="710" fill="var(--paper)"/>
    <!-- back side: panel and curved top band -->
    <rect class="back-panel" x="629" y="244" width="463" height="728" fill="var(--cyan)"/>
    <path class="back-top-band" d="M629 211 L1040 211 Q1080 211 1084 240 Q1090 262 1092 290 L1092 272 Q1060 244 1030 244 L629 244 Z" fill="var(--navy)"/>
    <!-- large decorative disc across the fold -->
    <g class="fold-disc">
      <circle cx="600" cy="640" r="150" fill="var(--cyan)" clip-path="url(#front-clip)"/>
      <circle cx="600" cy="640" r="150" fill="var(--navy)" clip-path="url(#back-clip)"/>
    </g>
  </svg>

  <div class="brand brand--front">
    <span class="brand-dot"></span>
    <div class="brand-text">
      <div class="brand-name">BrisaCorp</div>
      <div class="brand-tagline">Consultoria em Seguros</div>
    </div>
  </div>

  <div class="brand brand--back">
    <span class="brand-dot"></span>
    <div class="brand-text">
      <div class="brand-name">BrisaCorp</div>
      <div class="brand-tagline">Consultoria em Seguros</div>
    </div>
  </div>

  <address class="contact">
    <p>Rua das Palmeiras, 120</p>
    <p>(11) 4000-1200</p>
    <p>(11) 4000-1300</p>
    <p>contato@brisacorp.com.br</p>
    <p class="web">www.brisacorp.com.br</p>
  </address>
</main>
</body>
</html>
```